Name of Business is Bright Path Mentor,
Business Card and Logo Design for a health coaching practice that brings together all aspects of living including breathing, meditation, heartfelt intentional living, oneness with others, compassion, nutrition, hydration and primary care physician.

Target Market(s)

People looking for holistic approach to optimal living.

Industry/Entity Type

Business

Contact Information for Business Card

Martin R.K. Dowell
CWC, CHEP, B-MQ
Bright Path Mentor
514 Birchwood Ave
Cedar Hollow Falls, OH 48917

Logo Text

Everything You Need Is Within You Now

```html
<!DOCTYPE html>
<html lang="en">
<head>
<meta charset="utf-8">
<title>Bright Path Mentor – Business Card</title>
<link rel="stylesheet" href="https://fonts.googleapis.com/css2?family=Lora:wght@400;700&display=swap">
<style>
  :root {
    --backdrop: #e4e4e2;
    --card: #ffffff;
    --ink: #555555;
    --ink-soft: #6a6a6a;
    --brand: #3fbfa3;
    --shadow: rgba(0, 0, 0, 0.14);
  }
  * { margin: 0; padding: 0; box-sizing: border-box; }
  html, body {
    width: 1200px;
    height: 873px;
    overflow: hidden;
    background: var(--backdrop);
  }
  .canvas {
    position: relative;
    width: 1200px;
    height: 873px;
  }
  .card {
    position: absolute;
    top: 293px;
    width: 500px;
    height: 286px;
    background: var(--card);
    box-shadow: 0 6px 18px var(--shadow);
    font-family: "Lora", Georgia, serif;
    color: var(--ink);
  }
  .card--front { left: 70px; }
  .card--back { left: 630px; }

  .brand-mark {
    display: flex;
    align-items: center;
    gap: 10px;
    font-family: "Lora", Georgia, serif;
    font-weight: 700;
    color: var(--brand);
  }
  .brand-mark__dot {
    border-radius: 50%;
    background: var(--brand);
    flex: none;
  }

  .card--front .brand-mark {
    position: absolute;
    left: 34px;
    top: 32px;
    font-size: 19px;
  }
  .card--front .brand-mark__dot { width: 14px; height: 14px; }

  .contacts {
    position: absolute;
    left: 34px;
    top: 82px;
    list-style: none;
  }
  .contacts__item {
    display: flex;
    align-items: flex-start;
    gap: 14px;
    font-size: 12px;
    line-height: 17px;
    color: var(--ink-soft);
    margin-bottom: 10px;
  }
  .contacts__icon {
    width: 14px;
    height: 14px;
    flex: none;
    margin-top: 1px;
    fill: var(--ink-soft);
  }

  .holder {
    position: absolute;
    right: 34px;
    bottom: 30px;
    text-align: right;
  }
  .holder__name {
    font-size: 19px;
    font-weight: 400;
    color: var(--ink);
    margin-bottom: 6px;
  }
  .holder__line {
    font-size: 12px;
    line-height: 17px;
    color: var(--ink-soft);
  }

  .card--back .brand-mark {
    position: absolute;
    inset: 0;
    justify-content: center;
    font-size: 30px;
    gap: 14px;
  }
  .card--back .brand-mark__dot { width: 22px; height: 22px; }
</style>
</head>
<body>
<main class="canvas">

  <section class="card card--front" aria-label="Business card front">
    <div class="brand-mark">
      <span class="brand-mark__dot"></span>
      <span class="brand-mark__name">Bright Path Mentor</span>
    </div>

    <ul class="contacts">
      <li class="contacts__item">
        <svg class="contacts__icon" viewBox="0 0 16 16" aria-hidden="true">
          <path d="M3.6 1.2l2.3 2.6-1.3 1.9c.9 2 2.5 3.7 4.6 4.7l1.9-1.3 2.7 2.3-1.4 2.8C7 13.9 2.1 9 1 3.3z"/>
        </svg>
        <span>+00 (00) 98 765 43 21</span>
      </li>
      <li class="contacts__item">
        <svg class="contacts__icon" viewBox="0 0 16 16" aria-hidden="true">
          <path d="M1 3h14v10H1z M2 4.2v.6l6 4 6-4v-.6z" fill-rule="evenodd"/>
        </svg>
        <span>martin@brightpathmail.com</span>
      </li>
      <li class="contacts__item">
        <svg class="contacts__icon" viewBox="0 0 16 16" aria-hidden="true">
          <path d="M8 1.5L1 8h2v6.5h4v-4h2v4h4V8h2z"/>
        </svg>
        <span>514 Birchwood Ave<br>Cedar Hollow Falls, OH 48917</span>
      </li>
    </ul>

    <div class="holder">
      <p class="holder__name">Martin R.K. Dowell</p>
      <p class="holder__line">CWC, CHEP, B-MQ</p>
      <p class="holder__line">Bright Path Mentor</p>
    </div>
  </section>

  <section class="card card--back" aria-label="Business card back">
    <div class="brand-mark">
      <span class="brand-mark__dot"></span>
      <span class="brand-mark__name">Bright Path Mentor</span>
    </div>
  </section>

</main>
</body>
</html>
```